Vardek Hub, LLC. is the name of the company that will be an Internet startup working in E-commerce and

We are a new company and going to start the business by hiring people we need. We are on “Hiring Now…” status right now which we like to be displayed on the website homepage.
The website should allow us to start the hiring process with letting people see and apply for jobs posted on the website.

the company logo is attached.

Target Market(s)

Tech Job Seekers, Programmers, iOS and Android Developers, Software engineers, Graphic designers, QA engineers, Customer Service Reps,...

Industry/Entity Type

Internet

Number of Pages Required

5+ page

Font styles to use
Serif
Sans Serif

Colors

Designer to choose colors to be used in the design.

Requirements
Must have
• We need a system to help job seekers to upload the resume and cover letter and fill the required forms and answer some questions on a form designed to evaluate the job seekers and let them know if they fit in the position and should apply for it.
• We also want job seekers to do a Pre-Employment Tests including Aptitude, Personality, and Skills after they qualified for a job which links our website to web-based pre-employment testing services websites like (Quorva, Pellmark, Brumhall & Associates, Tolvin Assessment, …)

```html
<!DOCTYPE html>
<html lang="en">
<head>
<meta charset="utf-8">
<title>Vardek Hub — Hiring Now</title>
<link rel="stylesheet" href="https://fonts.googleapis.com/css2?family=Open+Sans:wght@400;600;700&display=swap">
<style>
:root{
  --blue:#2a7fc0;
  --blue-dark:#1f6ea8;
  --orange:#f05a1a;
  --orange-dark:#e2480b;
  --ink:#222;
  --muted:#777;
  --card:#efefef;
  --border:#d9d9d9;
  --bar:#333333;
  --footer:#e9e9e9;
  --white:#fff;
}
*{box-sizing:border-box;margin:0;padding:0}
html,body{width:1200px;height:2290px;overflow:hidden;background:var(--white);font-family:"Open Sans",Arial,sans-serif;color:var(--ink)}
.page{position:relative;width:1200px;height:2290px}

/* header */
.site-header{position:absolute;top:0;left:0;width:1200px;height:122px;background:var(--white)}
.brand{position:absolute;left:131px;top:44px;display:flex;align-items:center;gap:10px;font-size:30px;font-weight:700;color:var(--blue);letter-spacing:-.5px}
.brand-mark{width:16px;height:16px;background:var(--orange)}
.main-nav{position:absolute;top:57px;left:446px;font-size:12px}
.main-nav a{position:absolute;white-space:nowrap;color:var(--ink);text-decoration:none}
.main-nav a.active{color:var(--blue)}
.nav-divider{position:absolute;left:872px;top:42px;width:1px;height:48px;background:var(--border)}
.hiring{position:absolute;left:895px;top:46px;font-size:27px;color:var(--orange);font-weight:400;white-space:nowrap}

/* hero */
.hero{position:absolute;top:122px;left:0;width:1200px;height:492px;background:linear-gradient(100deg,#8e9498 0%,#b9bdc0 30%,#d4d6d7 55%,#c9c7c4 75%,#b79b84 100%)}
.hero-form{position:absolute;left:707px;top:172px;width:360px}
.hero-title{font-size:24px;font-weight:700;color:var(--white);text-align:center;margin-bottom:12px}
.hero-input{height:45px;background:var(--white);border-radius:2px;padding:0 24px;line-height:45px;font-size:12px;color:#555}
.hero-actions{display:flex;justify-content:space-between;margin-top:6px}
.btn-hero{width:176px;height:43px;line-height:43px;text-align:center;color:var(--white);font-size:14px;border-radius:2px}
.btn-hero.upload{background:linear-gradient(var(--blue),var(--blue-dark))}
.btn-hero.letter{background:linear-gradient(var(--orange),var(--orange-dark))}
.hero-arrow{position:absolute;top:354px;width:24px;height:24px}
.hero-arrow.prev{left:36px}
.hero-arrow.next{left:1140px}

/* featured */
.section-title{position:absolute;left:131px;top:688px;font-size:25px;color:var(--orange);font-weight:400}
.view-all{position:absolute;left:1018px;top:696px;width:48px;height:16px;border:1px solid var(--border);font-size:9px;color:var(--muted);text-align:center;line-height:14px}
.job-card{position:absolute;width:217px;height:216px;background:var(--card);padding:17px 20px 0}
.job-title{font-size:15.5px;line-height:21px;color:var(--blue);font-weight:400;white-space:nowrap}
.job-date{font-size:10.5px;line-height:14px;margin-top:8px;color:var(--ink);white-space:nowrap}
.job-text{font-size:11px;line-height:18px;color:var(--muted);margin-top:10px;white-space:nowrap}
.btn-apply{position:absolute;left:20px;top:158px;width:89px;height:36px;border:1px solid var(--blue);background:var(--white);color:var(--blue);font-size:12px;text-align:center;line-height:34px;border-radius:2px}

/* tests */
.tests{position:absolute;top:1280px;left:0;width:1200px;height:432px;background:linear-gradient(90deg,#c7c9ca 0%,#b4b7b9 45%,#c9cbcc 70%,#dcdddd 100%)}
.tests-title{position:absolute;left:473px;top:108px;font-size:24px;font-weight:400;color:var(--ink)}
.test-link{position:absolute;left:476px;width:248px;height:47px;background:rgba(255,255,255,.82);display:flex;align-items:center;gap:12px;padding-left:12px;font-size:19px;font-weight:700;color:var(--blue-dark);letter-spacing:.3px}
.test-link svg{width:20px;height:20px;fill:var(--blue-dark)}

/* companies */
.companies-title{position:absolute;top:1786px;left:0;width:1200px;text-align:center;font-size:17px;font-weight:400}
.company-row{position:absolute;top:1836px;left:131px;width:936px;display:flex;justify-content:space-between;align-items:center}
.company{font-size:20px;font-weight:700;color:#2a2a2a;letter-spacing:.5px}

/* newsletter */
.newsletter{position:absolute;top:1953px;left:0;width:1200px;height:79px;background:var(--bar)}
.newsletter-label{position:absolute;left:131px;top:24px;display:flex;align-items:center;gap:10px;color:var(--white);font-size:22px;font-weight:700}
.newsletter-label svg{width:24px;height:24px}
.newsletter-input{position:absolute;left:479px;top:22px;width:225px;height:34px;background:var(--white);font-size:12px;line-height:34px;padding-left:14px}
.newsletter-btn{position:absolute;left:704px;top:22px;width:127px;height:34px;background:var(--blue);color:var(--white);font-size:11px;line-height:34px;text-align:center}
.social{position:absolute;top:21px;width:38px;height:38px;border:1.5px solid var(--white);border-radius:50%}

/* footer */
.site-footer{position:absolute;top:2032px;left:0;width:1200px;height:258px;background:var(--footer)}
.footer-col{position:absolute;top:36px}
.footer-col h4{font-size:18px;font-weight:400;margin-bottom:8px}
.footer-col li{list-style:none;font-size:10.5px;line-height:20.6px;color:#444;white-space:nowrap}
.footer-col li::before{content:"• ";}
.footer-rule{position:absolute;left:131px;top:197px;width:936px;height:1px;background:#c9c9c9}
.copyright{position:absolute;top:218px;left:0;width:1200px;text-align:center;font-size:11px}
</style>
</head>
<body>
<div class="page">

<header class="site-header">
  <div class="brand"><span>Vardek Hub</span><span class="brand-mark"></span></div>
  <nav class="main-nav">
    <a class="active" style="left:0">Job Categories</a>
    <a style="left:111px">Companies</a>
    <a style="left:204px">Pre-Employment Test</a>
    <a style="left:357px">Support</a>
  </nav>
  <div class="nav-divider"></div>
  <div class="hiring">Hiring Now...</div>
</header>

<section class="hero" role="img" aria-label="Photo of a smiling young man in a dark suit at a job interview across from a woman">
  <svg class="hero-arrow prev" viewBox="0 0 24 24"><path d="M15 3 L6 12 L15 21" fill="none" stroke="#fff" stroke-width="2.5"/></svg>
  <svg class="hero-arrow next" viewBox="0 0 24 24"><path d="M9 3 L18 12 L9 21" fill="none" stroke="#fff" stroke-width="2.5"/></svg>
  <div class="hero-form">
    <h1 class="hero-title">Aliquam consectetur orci</h1>
    <div class="hero-input">Email Address</div>
    <div class="hero-actions">
      <div class="btn-hero upload">Upload Resume</div>
      <div class="btn-hero letter">Cover Letter</div>
    </div>
  </div>
</section>

<h2 class="section-title">Featured Jobs</h2>
<div class="view-all">View All</div>

<article class="job-card" style="left:133px;top:744px"><h3 class="job-title">Phasellus nisl est, condi<br>mentum vitae faucibus</h3><p class="job-date">11 September, 2017</p><p class="job-text">congue, tincidunt vulputate erat.<br>Aliquam consectetur orci moles<br>tie dictum molestie.</p><div class="btn-apply">Apply Now</div></article>
<article class="job-card" style="left:372px;top:744px"><h3 class="job-title">Phasellus nisl est, condi<br>mentum vitae faucibus</h3><p class="job-date">11 September, 2017</p><p class="job-text">congue, tincidunt vulputate erat.<br>Aliquam consectetur orci moles<br>tie dictum molestie.</p><div class="btn-apply">Apply Now</div></article>
<article class="job-card" style="left:611px;top:744px"><h3 class="job-title">Phasellus nisl est, condi<br>mentum vitae faucibus</h3><p class="job-date">11 September, 2017</p><p class="job-text">congue, tincidunt vulputate erat.<br>Aliquam consectetur orci moles<br>tie dictum molestie.</p><div class="btn-apply">Apply Now</div></article>
<article class="job-card" style="left:850px;top:744px"><h3 class="job-title">Phasellus nisl est, condi<br>mentum vitae faucibus</h3><p class="job-date">11 September, 2017</p><p class="job-text">congue, tincidunt vulputate erat.<br>Aliquam consectetur orci moles<br>tie dictum molestie.</p><div class="btn-apply">Apply Now</div></article>
<article class="job-card" style="left:133px;top:983px"><h3 class="job-title">Phasellus nisl est, condi<br>mentum vitae faucibus</h3><p class="job-date">11 September, 2017</p><p class="job-text">congue, tincidunt vulputate erat.<br>Aliquam consectetur orci moles<br>tie dictum molestie.</p><div class="btn-apply">Apply Now</div></article>
<article class="job-card" style="left:372px;top:983px"><h3 class="job-title">Phasellus nisl est, condi<br>mentum vitae faucibus</h3><p class="job-date">11 September, 2017</p><p class="job-text">congue, tincidunt vulputate erat.<br>Aliquam consectetur orci moles<br>tie dictum molestie.</p><div class="btn-apply">Apply Now</div></article>
<article class="job-card" style="left:611px;top:983px"><h3 class="job-title">Phasellus nisl est, condi<br>mentum vitae faucibus</h3><p class="job-date">11 September, 2017</p><p class="job-text">congue, tincidunt vulputate erat.<br>Aliquam consectetur orci moles<br>tie dictum molestie.</p><div class="btn-apply">Apply Now</div></article>
<article class="job-card" style="left:850px;top:983px"><h3 class="job-title">Phasellus nisl est, condi<br>mentum vitae faucibus</h3><p class="job-date">11 September, 2017</p><p class="job-text">congue, tincidunt vulputate erat.<br>Aliquam consectetur orci moles<br>tie dictum molestie.</p><div class="btn-apply">Apply Now</div></article>

<section class="tests" role="img" aria-label="Photo of a young man in a white shirt working on a laptop in a bright office with a bookshelf">
  <h2 class="tests-title">Pre-Employment Tests</h2>
  <div class="test-link" style="top:157px"><svg viewBox="0 0 20 20"><path d="M3 6h5V3h4v3h5v5h-3v3h3v3H3z"/></svg>APTITUDE TESTS</div>
  <div class="test-link" style="top:213px"><svg viewBox="0 0 20 20"><circle cx="10" cy="6" r="4"/><path d="M2 19c0-5 4-7 8-7s8 2 8 7z"/></svg>PERSONALITY TESTS</div>
  <div class="test-link" style="top:268px"><svg viewBox="0 0 20 20"><path d="M2 2h1.5v14.5H18V18H2z"/><rect x="5" y="10" width="2.5" height="5"/><rect x="9" y="6" width="2.5" height="9"/><rect x="13" y="8" width="2.5" height="7"/></svg>SKILLS</div>
</section>

<h2 class="companies-title">Companies</h2>
<div class="company-row">
  <span class="company">Tidelyn</span>
  <span class="company">Corvane</span>
  <span class="company">Brisket</span>
  <span class="company">Marwell</span>
  <span class="company">Juniva</span>
  <span class="company">Pellora</span>
  <span class="company">Stonebay</span>
</div>

<section class="newsletter">
  <div class="newsletter-label"><svg viewBox="0 0 24 24"><rect x="2" y="5" width="20" height="14" fill="none" stroke="#fff" stroke-width="2"/><path d="M2 6l10 7 10-7" fill="none" stroke="#fff" stroke-width="2"/></svg>NEWSLETTER SUBSCRIBE</div>
  <div class="newsletter-input">Email Address</div>
  <div class="newsletter-btn">SUBSCRIBE NOW</div>
  <div class="social" style="left:932px"></div>
  <div class="social" style="left:980px"></div>
  <div class="social" style="left:1028px"></div>
</section>

<footer class="site-footer">
  <div class="footer-col" style="left:133px"><h4>Links</h4><ul><li>Job Categories</li><li>Companies</li><li>Pre-Employment Test</li><li>Support</li></ul></div>
  <div class="footer-col" style="left:308px"><h4>Links</h4><ul><li>Phasellus nisl</li><li>Etiam vel</li><li>Aenean placerat</li><li>Vestibulum</li><li>Aenean faucibus</li></ul></div>
  <div class="footer-col" style="left:476px"><h4>Links</h4><ul><li>Phasellus nisl</li><li>Etiam vel</li><li>Aenean placerat</li><li>Vestibulum</li><li>Aenean faucibus</li></ul></div>
  <div class="footer-col" style="left:644px"><h4>Links</h4><ul><li>Phasellus nisl</li><li>Etiam vel</li><li>Aenean placerat</li><li>Vestibulum</li><li>Aenean faucibus</li></ul></div>
  <div class="footer-col" style="left:811px"><h4>Links</h4><ul><li>Phasellus nisl</li><li>Etiam vel</li><li>Aenean placerat</li><li>Vestibulum</li><li>Aenean faucibus</li></ul></div>
  <div class="footer-col" style="left:977px"><h4>Links</h4><ul><li>Phasellus nisl</li><li>Etiam vel</li><li>Aenean placerat</li><li>Vestibulum</li><li>Aenean faucibus</li></ul></div>
  <div class="footer-rule"></div>
  <p class="copyright">Copyright © 2017 Vardek Hub. All rights reserved.</p>
</footer>

</div>
</body>
</html>
```